Brightway Haul & Repair Services, are a company that offers a 'one stop shop' pre-move clean up a

I have already selected a logo which I would like on the front of the business cards along with phone numbers, web address and email which are:
0419574302
www.brightwayhaul.com.au
brightwayhaulrepair@mailbox.example

On the back of the card I would like to list some of the types of service we offer (clean - move - repairs/maintenance) which are:
CLEAN - windows, gutters, solar panels, driveways/paths, carpets.
MOVE - Small/medium size house/office moves, large item pick-up & delivery, yard clean-up and removal.
General maintenance and repairs.

I would like the blue logo on a gray background.

Thanks

```html
<!DOCTYPE html>
<html lang="en">
<head>
<meta charset="utf-8">
<title>Brightway Haul &amp; Repair Services – Business Card</title>
<link rel="stylesheet" href="https://fonts.googleapis.com/css2?family=Open+Sans:wght@400;600;700;800&display=swap">
<style>
  :root {
    --page: #ffffff;
    --card-light: #fafafa;
    --card-mid: #e4e4e4;
    --card-edge: #c9c9c9;
    --brand-blue: #2f71ea;
    --text-blue: #2c6fdc;
    --panel-blue: #2f74f2;
    --panel-text: #ffffff;
  }
  * { box-sizing: border-box; margin: 0; padding: 0; }
  html, body {
    width: 893px;
    height: 1200px;
    overflow: hidden;
    background: var(--page);
    font-family: "Open Sans", Arial, sans-serif;
  }
  .canvas {
    position: relative;
    width: 893px;
    height: 1200px;
  }
  .card {
    position: absolute;
    left: 46px;
    width: 786px;
    height: 507px;
    background: radial-gradient(ellipse at 50% 40%, var(--card-light) 0%, var(--card-mid) 55%, var(--card-edge) 100%);
  }
  .card--front { top: 52px; }
  .card--back { top: 628px; }

  .brand-name {
    position: absolute;
    left: 0;
    right: 0;
    top: 150px;
    text-align: center;
    color: var(--brand-blue);
    font-weight: 800;
    text-transform: uppercase;
    line-height: 1;
  }
  .brand-name__main {
    display: block;
    font-size: 66px;
    letter-spacing: 1px;
  }
  .brand-name__sub {
    display: block;
    margin-top: 14px;
    font-size: 30px;
    letter-spacing: 1px;
  }

  .contact {
    position: absolute;
    left: 0;
    right: 0;
    top: 388px;
    text-align: center;
    color: var(--text-blue);
    font-weight: 600;
    font-size: 31px;
    line-height: 47px;
  }

  .services-title {
    position: absolute;
    left: 42px;
    top: 32px;
    color: var(--text-blue);
    font-weight: 600;
    font-size: 48px;
    line-height: 1;
  }
  .services-panel {
    position: absolute;
    left: 24px;
    top: 99px;
    width: 738px;
    height: 371px;
    border-radius: 30px;
    background: var(--panel-blue);
    color: var(--panel-text);
    text-align: center;
    font-size: 31px;
    line-height: 44px;
    padding: 28px 16px 0;
  }
  .services-panel p + p { margin-top: 12px; }
  .services-panel .service--general { margin-top: 26px; padding-left: 70px; }
</style>
</head>
<body>
<main class="canvas">
  <section class="card card--front" aria-label="Card front">
    <h1 class="brand-name">
      <span class="brand-name__main">Brightway Haul</span>
      <span class="brand-name__sub">&amp; Repair Services</span>
    </h1>
    <p class="contact">
      P: 0419574302 www.brightwayhaul.com.au<br>
      brightwayhaulrepair@mailbox.example
    </p>
  </section>

  <section class="card card--back" aria-label="Card back">
    <h2 class="services-title">Services we offer</h2>
    <div class="services-panel">
      <p class="service">CLEAN - windows, gutters, solar panels,<br>driveways/paths, carpets.</p>
      <p class="service">MOVE - Small/medium size house/office<br>moves, large item pick-up &amp; delivery, yard<br>clean-up and removal.</p>
      <p class="service service--general">General maintenance and repairs.</p>
    </div>
  </section>
</main>
</body>
</html>
```